Website for Architecture & Interior Design firm

We are architecture and interior design firm looking for website design, word press based, smooth, elegant and easy to use for visitors. It should be easy to navigate using a mobile phone, with the ability to change pictures easily. It is a Bilingual website, (English: left to right, Arabic: right to left). A button in the menu bar is required to change the language, At first, we expect an English version, then we will help the designer by providing Arabic translation for any part of the website. Our website main purpose is to display our works in a picture format (Portfolio) to our clients, which mainly consist of four galleries from our (Services) as follow: 1- Architecture 2- Interior Design 3- Project Management 4- Importing from Abroad - Each service will have its page, which displays projects(items) in thumbnail format with simple text, which deploys (when clicked) into Fullscreen gallery to show the items related pictures (Dark gray or black background). - Navigation buttons/arrows are required, (X) button to close the navigation. - This is a very important part, the user experience in PC/Browser mode or Mobile mode should be easy, error-free and fast. Our homepage consists of four main elements: A- Edge to edge picture (Changing in a smooth transitional way, Random pictures from our Services) with our Logo, also persistent menu bar in the top (Home | About Us | Architecture | Interior design | Project Management | Importing from Abroad) + Social media icons B- Photo tiles (Random pictures from our Services) C- Our Services in a fixed 4-tile picture (Clickable) D- Contact Section (Simple name, contact number, message form) We expect the final service should be: 1- a fully functioning website, WordPress based, ready to be used by visitors 2- full content filling, we will contact the designer and provide the material (texture, text,etc..)
Colors
Designer to choose colors to be used in the design.
Look and feel
Each slider illustrates characteristics of the customer's brand and the style your logo design should communicate.

```html
<!DOCTYPE html>
<html lang="en">
<head>
<meta charset="utf-8">
<title>Meridian Studio — Architecture &amp; Interior Design</title>
<link rel="stylesheet" href="https://fonts.googleapis.com/css2?family=Montserrat:wght@400;500;600;700&family=Open+Sans:wght@400;600&display=swap">
<style>
:root{
  --accent:#29a8e0;
  --panel:#3e4347;
  --panel-dark:#2f3337;
  --ink:#3a3d40;
  --muted:#8d9296;
  --line:#d9dcde;
  --page:#f4f5f6;
  --white:#ffffff;
  --footer:#2b2e31;
}
*{box-sizing:border-box;margin:0;padding:0}
html,body{width:1200px;height:3372px;overflow:hidden}
body{position:relative;background:var(--page);font-family:"Open Sans",Arial,sans-serif;color:var(--ink)}

/* top bar */
.topbar{position:absolute;left:0;top:0;width:1200px;height:26px;background:var(--white);z-index:5;display:flex;align-items:center;justify-content:space-between;padding:0 78px}
.topbar nav{display:flex;gap:26px;font-family:"Montserrat",sans-serif;font-size:11px;color:var(--ink)}
.topbar nav a{text-decoration:none;color:inherit;position:relative}
.topbar nav a.active{color:var(--accent)}
.dropdown{position:absolute;left:134px;top:26px;width:96px;background:var(--white);padding:8px 10px;font-family:"Montserrat",sans-serif;font-size:9px;line-height:2.6;color:var(--ink);z-index:6;box-shadow:0 2px 6px rgba(0,0,0,.15)}
.dropdown span{display:block;border-bottom:1px solid var(--line)}
.social{display:flex;gap:10px}
.social i{display:block;width:10px;height:10px;border-radius:50%;background:var(--ink)}

/* hero */
.hero{position:absolute;left:0;top:26px;width:1200px;height:394px;background:linear-gradient(180deg,#1d2a30 0%,#4a5e68 45%,#2a3438 100%)}
.brand{position:absolute;left:0;top:40px;width:1200px;text-align:center;color:var(--white);font-family:"Montserrat",sans-serif}
.brand .mark{display:block;width:34px;height:34px;margin:0 auto 12px;background:var(--accent)}
.brand .name{font-size:20px;font-weight:500;letter-spacing:3px}
.hero h1{position:absolute;left:0;top:232px;width:1200px;text-align:center;font-family:"Montserrat",sans-serif;font-weight:500;font-size:64px;letter-spacing:6px;color:var(--white)}
.hero .tagline{position:absolute;left:0;top:318px;width:1200px;text-align:center;font-family:"Montserrat",sans-serif;font-size:16px;letter-spacing:10px;color:rgba(255,255,255,.35)}

/* about */
.about{position:absolute;left:0;top:420px;width:1200px;height:420px;background:var(--white)}
.about h2{position:absolute;left:146px;top:84px;font-family:"Montserrat",sans-serif;font-weight:700;font-size:28px;color:var(--ink)}
.about p{position:absolute;left:146px;top:136px;width:330px;font-size:14px;line-height:22px;color:var(--muted)}
.btn{display:inline-block;background:var(--accent);color:var(--white);font-family:"Montserrat",sans-serif;font-weight:600;font-size:11px;letter-spacing:2px;padding:9px 28px}
.about .btn{position:absolute;left:146px;top:286px;width:170px;text-align:center}
.about-photo{position:absolute;left:520px;top:376px;width:530px;height:372px;background:linear-gradient(160deg,#c9cdd0 0%,#8d8476 55%,#5d5a55 100%);box-shadow:0 10px 24px rgba(0,0,0,.3);z-index:3}

/* stats */
.stats{position:absolute;left:0;top:840px;width:1200px;height:250px;background:var(--white)}
.stat{position:absolute;top:56px;width:220px;height:80px;border-bottom:1px solid var(--line)}
.stat svg{position:absolute;left:0;top:6px}
.stat .num{position:absolute;left:60px;top:0;font-family:"Montserrat",sans-serif;font-weight:700;font-size:44px;line-height:48px;color:var(--ink)}
.stat .label{position:absolute;left:62px;top:50px;font-family:"Montserrat",sans-serif;font-size:10px;letter-spacing:1.5px;color:var(--muted)}

/* services */
.services{position:absolute;left:88px;top:1172px;width:1024px;height:1600px;display:grid;grid-template-columns:512px 512px;grid-template-rows:repeat(4,400px)}
.tile{position:relative;background:var(--panel);color:var(--white);text-align:center;padding-top:118px}
.tile h3{font-family:"Montserrat",sans-serif;font-weight:500;font-size:32px;letter-spacing:3px;color:#9ea4a8;line-height:38px;text-transform:uppercase}
.tile p{width:300px;margin:16px auto 16px;font-size:12px;line-height:17px;color:#d9dcde}
.photo{width:512px;height:400px}
.photo.arch{background:linear-gradient(135deg,#eef0f1 0%,#b9bec2 50%,#dfe2e4 100%)}
.photo.interior{background:linear-gradient(160deg,#e7ddd0 0%,#b49a7c 50%,#5e5045 100%)}
.photo.pm{background:linear-gradient(150deg,#f1f3f5 0%,#c7d0d8 60%,#8fa0b0 100%)}
.photo.import{background:linear-gradient(180deg,#5a5a7a 0%,#8f6f6a 50%,#3b3a44 100%)}

/* contact */
.contact{position:absolute;left:0;top:2840px;width:1200px;height:380px}
.contact h2{position:absolute;left:176px;top:92px;font-family:"Montserrat",sans-serif;font-weight:500;font-size:44px;letter-spacing:2px;color:var(--accent)}
.contact ul{position:absolute;left:216px;top:158px;list-style:none;font-size:11px;line-height:29px;color:var(--muted)}
.contact li{display:flex;align-items:center;gap:14px}
.contact li svg{flex:none}
.form{position:absolute;left:600px;top:0;width:508px;height:372px;background:var(--panel);padding:20px 16px;font-family:"Montserrat",sans-serif;font-size:11px;color:var(--white)}
.form label{display:block;margin-bottom:6px;font-weight:600}
.form .field{width:220px;height:24px;border:1px solid #7f868b;margin-bottom:16px}
.form .field.message{height:120px}
.form .send{display:block;width:180px;height:22px;background:var(--accent);margin-top:10px;text-align:center;line-height:22px;font-size:10px;letter-spacing:1px}

/* footer */
.footer{position:absolute;left:0;top:3312px;width:1200px;height:60px;background:var(--footer);display:flex;align-items:center;justify-content:space-between;padding:0 60px;font-size:10px;color:#9aa0a4}
.footer nav{display:flex;gap:14px;color:#c7cbce}
</style>
</head>
<body>

<header class="topbar">
  <nav>
    <a>Home</a><a class="active">Services</a><a>Contact</a><a>About</a><a>AR</a>
  </nav>
  <div class="social"><i></i><i></i><i></i><i></i></div>
</header>
<div class="dropdown">
  <span>Architecture</span><span>Interior Design</span><span>Project Management</span><span>Importing from Abroad</span>
</div>

<section class="hero" role="img" aria-label="Full-width photo of modern towers seen from below">
  <div class="brand"><span class="mark"></span><span class="name">MERIDIAN STUDIO</span></div>
  <h1>HEADER TITLE</h1>
  <div class="tagline">ARCHITECTURE &amp; DESIGN</div>
</section>

<section class="about">
  <h2>About Us</h2>
  <p>We shape buildings and interiors with care, balance and light. Our studio guides every project from first sketch to final detail, creating calm spaces that feel made for the people who live in them.</p>
  <a class="btn">LEARN MORE</a>
</section>
<div class="about-photo" role="img" aria-label="Photo of a tall office building against the sky"></div>

<section class="stats">
  <div class="stat" style="left:140px">
    <svg width="44" height="34" viewBox="0 0 44 34"><rect x="2" y="4" width="40" height="26" rx="3" fill="none" stroke="#29a8e0" stroke-width="3"/><rect x="10" y="12" width="24" height="10" fill="#29a8e0"/></svg>
    <div class="num">255</div><div class="label">FINISHED PROJECTS</div>
  </div>
  <div class="stat" style="left:480px">
    <svg width="44" height="40" viewBox="0 0 44 40"><circle cx="22" cy="11" r="9" fill="#29a8e0"/><path d="M4 40c0-11 8-18 18-18s18 7 18 18z" fill="#29a8e0"/></svg>
    <div class="num">99</div><div class="label">SATISFIED CUSTOMERS</div>
  </div>
  <div class="stat" style="left:820px">
    <svg width="44" height="34" viewBox="0 0 44 34"><path d="M2 18l10-10 10 6 10-6 10 10-10 10-10-6-10 6z" fill="none" stroke="#29a8e0" stroke-width="3" stroke-linejoin="round"/></svg>
    <div class="num">15</div><div class="label">YEARS OF EXPERIENCE</div>
  </div>
</section>

<section class="services">
  <div class="tile">
    <h3>Architecture</h3>
    <p>Thoughtful buildings planned from concept to completion, with clear forms and lasting materials for every site.</p>
    <a class="btn">LEARN MORE</a>
  </div>
  <div class="photo arch" role="img" aria-label="Photo of a white geometric building facade"></div>
  <div class="photo interior" role="img" aria-label="Photo of a warm living room with shelving"></div>
  <div class="tile">
    <h3>Interior-Design</h3>
    <p>Interiors that feel calm and personal, combining light, texture and furniture into spaces made for daily living.</p>
    <a class="btn">LEARN MORE</a>
  </div>
  <div class="tile">
    <h3>Project<br>Management</h3>
    <p>We lead schedules, budgets and teams on site so each project is delivered on time and to a high standard.</p>
    <a class="btn">LEARN MORE</a>
  </div>
  <div class="photo pm" role="img" aria-label="Photo of hands reviewing project documents"></div>
  <div class="photo import" role="img" aria-label="Photo of a modern villa with a pool at dusk"></div>
  <div class="tile">
    <h3>Importing from<br>Abroad</h3>
    <p>Selected furniture, fittings and finishes sourced from trusted makers abroad and delivered to your project.</p>
    <a class="btn">LEARN MORE</a>
  </div>
</section>

<section class="contact">
  <h2>CONTACT US</h2>
  <ul>
    <li><svg width="12" height="16" viewBox="0 0 12 16"><path d="M6 0a6 6 0 0 0-6 6c0 4 6 10 6 10s6-6 6-10a6 6 0 0 0-6-6z" fill="#8d9296"/><circle cx="6" cy="6" r="2" fill="#f4f5f6"/></svg>14 Harbor Lane, Westgate, Suite 200</li>
    <li><svg width="14" height="10" viewBox="0 0 14 10"><rect x=".5" y=".5" width="13" height="9" fill="none" stroke="#8d9296"/><path d="M.5 .5l6.5 5 6.5-5" fill="none" stroke="#8d9296"/></svg>hello@meridianstudio.com</li>
    <li><svg width="14" height="14" viewBox="0 0 14 14"><path d="M3 1l3 3-2 2a8 8 0 0 0 4 4l2-2 3 3-2 2C5 13 1 9 1 3z" fill="#8d9296"/></svg>+00 555 0142</li>
    <li><svg width="14" height="14" viewBox="0 0 14 14"><path d="M3 1l3 3-2 2a8 8 0 0 0 4 4l2-2 3 3-2 2C5 13 1 9 1 3z" fill="#8d9296"/></svg>+00 555 0178</li>
  </ul>
  <div class="form">
    <label>Your Name</label><div class="field"></div>
    <label>Your Email</label><div class="field"></div>
    <label>Your Message</label><div class="field message"></div>
    <span class="send">SEND</span>
  </div>
</section>

<footer class="footer">
  <span>Copyright © Meridian Studio. All rights reserved</span>
  <nav><span>Home</span><span>Architecture</span><span>Interior Design</span><span>Project Management</span><span>Importing from Abroad</span><span>Contact</span><span>About</span></nav>
</footer>

</body>
</html>
```